依頼詳細
『Velva Prism ヴェルヴァプリズム』のアルミ袋デザインを依頼させて頂きます。

商品サイトがありますのでこのサイトにイメージを合わせて頂けたらと思います。
商品サイト  http://velvaprism-shop.net/item/

参考画像も貼っておきます。

色数は背景含めて3色でお願いします。
希望イメージは薄いピンクで背景はグラデーションをかけて下さい。
花や葉っぱなど、上品な感じの模様を背景に少し入れて下さい。(参考画像のような柄でお願いします)
記載項目
サブタイトル: 30歳を過ぎたらフルボディケア

商品名: Velva Prism  ヴェルヴァプリズム ← ローマ字の方を大きめに目立つように記載してほしいです。

プラセンタ、コラーゲン、ヒアルロン酸、プエラリア、ローヤルゼリー、
はと麦、真珠パウダーなどあらゆる美容成分をオールインワンにしました。←下の方にいれてほしい文章です。

1袋90粒入り
希望イメージ
シンプル 複雑
単色 カラフル
暗い 明るい
日常 高級
遊び心 厳粛
未来的 伝統的
女性的 男性的
希望する色
ピンク、白等で優しく綺麗な感じでお願いします。
納品ファイル
• イラストレーター形式 (.ai)
• フォトショップ形式 (.psd)
補足説明
依頼公開後の追記内容
■ 選んだ理由

ピンクと白を使った優しく上品な感じが、こちらのイメージとぴったり
あっていましたので選ばせて頂きました。

■ 提案者全員のお礼・コメント

たくさんの提案を本当にありがとうございました。
色んなタイプがあり、とても迷いました。
今回のイメージに合う提案もたくさんあり、本当に
ありがとうございました。

```html
<!DOCTYPE html>
<html lang="ja">
<head>
<meta charset="utf-8">
<title>Velva Prism ヴェルヴァプリズム</title>
<link rel="stylesheet" href="https://fonts.googleapis.com/css2?family=Noto+Sans+JP:wght@300;400&family=Playfair+Display:wght@400&display=swap">
<style>
  :root {
    --bg-top: #fbe3ea;
    --bg-mid: #f3a9c0;
    --bg-bottom: #e45a86;
    --panel: #f2c6c2;
    --panel-edge: #f2c6c2;
    --ink: #8b5a52;
    --ink-soft: #9c6d64;
  }
  html, body {
    margin: 0;
    padding: 0;
    width: 749px;
    height: 1200px;
    overflow: hidden;
  }
  .package {
    position: relative;
    width: 749px;
    height: 1200px;
    overflow: hidden;
    font-family: "Noto Sans JP", sans-serif;
    color: var(--ink);
  }
  .floral-backdrop {
    position: absolute;
    inset: 0;
    background: linear-gradient(180deg, var(--bg-top) 0%, var(--bg-mid) 45%, var(--bg-bottom) 100%);
  }
  .label-panel {
    position: absolute;
    left: 130px;
    top: 238px;
    width: 513px;
    height: 750px;
  }
  .label-frame {
    position: absolute;
    inset: 0;
  }
  .label-content {
    position: absolute;
    inset: 0;
    text-align: center;
  }
  .subtitle-arc {
    position: absolute;
    left: 0;
    top: 40px;
    width: 513px;
    height: 120px;
    overflow: visible;
  }
  .subtitle-arc text {
    font-family: "Noto Sans JP", sans-serif;
    font-weight: 300;
    font-size: 26px;
    letter-spacing: 2px;
    fill: var(--ink);
  }
  .product-name {
    position: absolute;
    left: 0;
    right: 0;
    top: 142px;
    margin: 0;
    font-family: "Playfair Display", serif;
    font-weight: 400;
    font-size: 76px;
    line-height: 1;
    letter-spacing: -1px;
    color: var(--ink);
  }
  .product-name-kana {
    position: absolute;
    left: 0;
    right: 0;
    top: 232px;
    margin: 0;
    font-weight: 300;
    font-size: 24px;
    line-height: 1;
    letter-spacing: 7px;
    color: var(--ink);
  }
  .square-row {
    position: absolute;
    left: 0;
    right: 0;
    top: 352px;
    display: flex;
    justify-content: center;
    gap: 42px;
  }
  .square-row span {
    width: 22px;
    height: 22px;
    background: var(--ink);
  }
  .ingredients {
    position: absolute;
    left: 40px;
    right: 40px;
    top: 420px;
    margin: 0;
    text-align: left;
    font-weight: 300;
    font-size: 17px;
    line-height: 1.9;
    letter-spacing: 0.5px;
    white-space: nowrap;
    color: var(--ink);
  }
  .count {
    position: absolute;
    left: 0;
    right: 0;
    top: 630px;
    margin: 0;
    font-weight: 300;
    font-size: 28px;
    line-height: 1;
    letter-spacing: 3px;
    color: var(--ink);
  }
</style>
</head>
<body>
  <main class="package">
    <div class="floral-backdrop" role="img" aria-label="淡いピンクから濃いピンクへのグラデーションに白とピンクの花柄を散りばめた背景"></div>

    <section class="label-panel">
      <svg class="label-frame" width="513" height="750" viewBox="0 0 513 750" aria-hidden="true">
        <rect x="8" y="8" width="497" height="734" fill="var(--panel)"/>
        <rect x="8" y="8" width="497" height="734" fill="none" stroke="var(--panel-edge)" stroke-width="14" stroke-dasharray="0 14" stroke-linecap="round"/>
        <rect x="26" y="26" width="461" height="698" fill="none" stroke="var(--ink-soft)" stroke-width="2" stroke-dasharray="6 5"/>
      </svg>

      <div class="label-content">
        <svg class="subtitle-arc" viewBox="0 0 513 120" aria-label="30歳過ぎたらフルボディケア">
          <path id="subtitle-path" d="M 40 105 Q 256 20 473 105" fill="none"/>
          <text text-anchor="middle"><textPath href="#subtitle-path" startOffset="50%">30歳過ぎたらフルボディケア</textPath></text>
        </svg>

        <h1 class="product-name">Velva Prism</h1>
        <p class="product-name-kana">ヴェルヴァプリズム</p>

        <div class="square-row" aria-hidden="true"><span></span><span></span><span></span></div>

        <p class="ingredients">プラセンタ、コラーゲン、ヒアルロン酸、プエラリア<br>ローヤルゼリー、はと麦、真珠パウダーなどあらゆる<br>美容成分をオールインワンにしました</p>

        <p class="count">90 粒入り</p>
      </div>
    </section>
  </main>
</body>
</html>
```